Crumble Cove Supper Invitation

We will be having a Fish Fry on May 17th from 6PM -10PM. Location is 4721 Larkspur Ln. Mansfield, TX 76058. We need a Invitation, which includes a the header reading "Crumble Cove Supper". Wording of "Crumble Cove Supper" should incorporate both baseball and food batter. Think baseball bats dripping in batter. Admission to all you can eat fish fry will be a donation of any baseball equipment including: bats, gloves, jerseys, cleats, balls, or financial donation. Proceeds will go towards funding Pemberly Family in traveling to Dominican Republic to conduct baseball ministries. It would great to incorporate Dominican Republic flag or colors.

```html
<!DOCTYPE html>
<html lang="en">
<head>
<meta charset="UTF-8">
<title>Crumble Cove Supper Invitation</title>
<link href="https://fonts.googleapis.com/css2?family=Anton&family=Oswald:wght@600&family=Poppins:wght@400;600;700&family=Roboto+Slab:wght@700;800;900&display=swap" rel="stylesheet">
<style>
  :root {
    --navy: #0e2548;
    --navy-deep: #0a1c38;
    --band: #0b2140;
    --red: #cf1429;
    --white: #ffffff;
    --concrete: #cfcfcf;
    --flag-blue: #1f4f9c;
    --flag-red: #c8202b;
  }
  * { margin: 0; padding: 0; box-sizing: border-box; }
  html, body { width: 912px; height: 1200px; overflow: hidden; background: #f2f2f2; }
  .invitation {
    position: relative; width: 912px; height: 1200px; overflow: hidden;
    background: radial-gradient(ellipse at 50% 60%, #143060 0%, var(--navy) 55%, var(--navy-deep) 100%);
    color: var(--white);
    font-family: "Poppins", sans-serif;
  }
  .layer { position: absolute; left: 0; top: 0; }
  .center { position: absolute; left: 0; width: 912px; text-align: center; }
  .slab { font-family: "Roboto Slab", serif; }

  .brand-mark {
    position: absolute; left: 215px; width: 482px; top: 128px;
    display: flex; align-items: center; justify-content: center; gap: 10px;
    font-family: "Roboto Slab", serif; font-weight: 800; font-size: 26px; color: var(--white);
  }
  .brand-mark .dot { width: 14px; height: 14px; border-radius: 50%; background: var(--white); }

  .invited { top: 265px; left: 215px; width: 482px; font-weight: 800; font-size: 17px; letter-spacing: 3px; }
  .title-main { top: 290px; left: 215px; width: 482px; font-family: "Anton", sans-serif; font-size: 72px; line-height: 86px; letter-spacing: 1px; }
  .title-sub { top: 380px; left: 215px; width: 482px; font-weight: 900; font-size: 50px; line-height: 56px; letter-spacing: 1px; }
  .tagline { top: 447px; left: 215px; width: 482px; height: 39px; line-height: 39px; font-family: "Oswald", sans-serif; font-weight: 600; font-size: 23px; }
  .tagline .sep { color: #f2b134; margin: 0 4px; }
  .stars { top: 493px; left: 215px; width: 482px; font-size: 20px; letter-spacing: 2px; }

  .date { position: absolute; left: 170px; top: 645px; font-weight: 900; font-size: 52px; line-height: 52px; }
  .divider { position: absolute; width: 1px; height: 98px; top: 655px; background: rgba(255,255,255,.55); }
  .time { position: absolute; left: 346px; top: 668px; }
  .time .label { font-weight: 900; font-size: 27px; color: var(--red); line-height: 32px; }
  .time .hours { font-weight: 900; font-size: 52px; line-height: 60px; }
  .place { position: absolute; left: 604px; top: 647px; }
  .place .label { font-weight: 900; font-size: 27px; color: var(--red); line-height: 36px; }
  .place .address { font-weight: 700; font-size: 14.5px; line-height: 20px; margin-top: 4px; }

  .rule { position: absolute; left: 170px; width: 570px; height: 1px; background: rgba(255,255,255,.6); }
  .all-you-can-eat { top: 793px; font-weight: 800; font-size: 22px; }
  .pill {
    position: absolute; left: 339px; top: 836px; width: 234px; height: 36px; border-radius: 18px;
    background: var(--red); text-align: center; line-height: 36px; font-family: "Roboto Slab", serif; font-weight: 800; font-size: 17px;
  }
  .donation { top: 883px; font-size: 23px; }
  .donation strong { font-weight: 700; }
  .gear { top: 919px; font-size: 20.5px; display: flex; justify-content: center; align-items: center; gap: 9px; }
  .gear svg { width: 14px; height: 14px; }
  .contribution { top: 952px; font-weight: 700; font-size: 27px; color: var(--red); }
  .why-title { top: 1016px; font-weight: 600; font-size: 12.5px; }
  .why-text { top: 1039px; font-size: 13.5px; line-height: 19px; color: #e6ebf3; }

  .join-bar { position: absolute; left: 163px; top: 1097px; width: 587px; height: 43px; border-radius: 14px; background: var(--white); border: 1.5px solid var(--red); overflow: hidden; display: flex; }
  .join-bar .cta { width: 135px; background: var(--red); font-family: "Roboto Slab", serif; font-weight: 800; font-size: 25px; line-height: 40px; text-align: center; }
  .join-bar .message { color: var(--navy); font-weight: 600; font-size: 15px; line-height: 40px; padding-left: 14px; }
</style>
</head>
<body>
<main class="invitation">
  <!-- concrete strip and torn edge -->
  <svg class="layer" width="912" height="1200" viewBox="0 0 912 1200" role="img" aria-label="Grey concrete texture">
    <defs>
      <linearGradient id="concreteTone" x1="0" y1="0" x2="1" y2="1">
        <stop offset="0" stop-color="#d9d9d9"/><stop offset="1" stop-color="#b9b9b9"/>
      </linearGradient>
    </defs>
    <polygon fill="url(#concreteTone)" points="697,0 912,0 912,220 880,224 860,232 835,236 812,240 790,250 770,252 748,258 725,262 710,266 697,268"/>
  </svg>

  <!-- red ribbon -->
  <svg class="layer" width="912" height="1200" viewBox="0 0 912 1200">
    <polygon fill="var(--red)" points="215,0 697,0 697,622 456,543 215,622"/>
    <rect x="215" y="447" width="482" height="39" fill="var(--band)"/>
  </svg>

  <!-- Dominican flag fabric areas -->
  <svg class="layer" width="912" height="1200" viewBox="0 0 912 1200" role="img" aria-label="Waving Dominican Republic flag">
    <defs>
      <linearGradient id="flagTone" x1="0" y1="0" x2="1" y2="1">
        <stop offset="0" stop-color="var(--flag-red)"/>
        <stop offset="0.3" stop-color="#f4f4f4"/>
        <stop offset="0.5" stop-color="var(--flag-blue)"/>
        <stop offset="0.75" stop-color="#e8e8e8"/>
        <stop offset="1" stop-color="var(--flag-red)"/>
      </linearGradient>
      <linearGradient id="flagCorner" x1="1" y1="0" x2="0" y2="1">
        <stop offset="0" stop-color="#e8602f"/><stop offset="0.5" stop-color="#f1f1f1"/><stop offset="1" stop-color="var(--flag-blue)"/>
      </linearGradient>
    </defs>
    <path fill="url(#flagTone)" d="M0,0 L486,0 C380,60 280,130 253,228 C240,290 228,340 215,420 C160,480 80,540 0,591 Z"/>
    <path fill="url(#flagCorner)" d="M912,1008 C880,1040 860,1090 872,1130 C850,1160 815,1185 779,1200 L912,1200 Z"/>
  </svg>

  <div class="brand-mark"><span class="dot"></span>Crumble Cove Supper</div>

  <p class="center slab invited">YOU ARE INVITED TO THE</p>
  <h1 class="center title-main">CRUMBLE COVE</h1>
  <p class="center slab title-sub">SUPPER</p>
  <p class="center tagline">EAT FISH<span class="sep">|</span>GIVE GEAR<span class="sep">|</span>CHANGE LIVES</p>
  <p class="center stars">★★★★★★★★★★★★★★★★★★</p>

  <p class="date slab">May<br>17th</p>
  <span class="divider" style="left:322px"></span>
  <div class="time slab"><p class="label">From</p><p class="hours">6-10PM</p></div>
  <span class="divider" style="left:580px"></span>
  <div class="place slab">
    <p class="label">Location</p>
    <p class="address">4721 Larkspur<br>Ln. Mansfield,<br>TX 76058</p>
  </div>

  <span class="rule" style="top:775px"></span>
  <p class="center slab all-you-can-eat">ALL-YOU-CAN-EAT FISH FRY!</p>
  <div class="pill">ADMISSION TO ALL</div>
  <p class="center donation">A DONATION OF <strong>BASEBALL EQUIPMENT</strong></p>
  <p class="center gear">
    <span>Bats</span>
    <svg viewBox="0 0 14 14"><circle cx="7" cy="7" r="7" fill="var(--red)"/><path d="M4 7.2l2 2 4-4" stroke="#fff" stroke-width="1.6" fill="none"/></svg>
    <span>Gloves</span>
    <svg viewBox="0 0 14 14"><circle cx="7" cy="7" r="7" fill="var(--red)"/><path d="M4 7.2l2 2 4-4" stroke="#fff" stroke-width="1.6" fill="none"/></svg>
    <span>Jerseys</span>
    <svg viewBox="0 0 14 14"><circle cx="7" cy="7" r="7" fill="var(--red)"/><path d="M4 7.2l2 2 4-4" stroke="#fff" stroke-width="1.6" fill="none"/></svg>
    <span>Cleats</span>
    <svg viewBox="0 0 14 14"><circle cx="7" cy="7" r="7" fill="var(--red)"/><path d="M4 7.2l2 2 4-4" stroke="#fff" stroke-width="1.6" fill="none"/></svg>
    <span>Balls</span>
  </p>
  <p class="center contribution">OR A FINANCIAL CONTRIBUTION</p>
  <span class="rule" style="top:999px"></span>

  <p class="center why-title">WHY IT MATTERS?</p>
  <p class="center why-text">All proceeds help the Pemberly Family travel to the Dominican Republic to<br>spread baseball ministry and impact young athletes' lives.</p>

  <div class="join-bar">
    <span class="cta">join us</span>
    <span class="message">For great food, community, and a great cause!</span>
  </div>
</main>
</body>
</html>
```